Keen Compass - Web Design Project

We need a website for our new company based in Sao Paulo - Brazil. Our initial product is Keen Compass - an online assessment system based on the most recent neuroscience academic research. The system gathers tests that are applied in the selection and evaluation of employees. We would like to see designs that use the colors black and blue. The final design should communicate trust. We like clean and simple designs.

Login to www.keencompass-example.com.br
login: user
pass: user

We need three pages:
1- Login page: http://www.keencompass-example.com.br/

2- Welcome page: http://www.keencompass-example.com.br/sys/admin/index.php

3- Results page: http://www.keencompass-example.com.br/sys/admin/admin_provas_resultados.php?unique_id=5

Our logo was created using ArtLoomly.
Next projetcs: Tests interface redesign.

Industry/Entity Type

It Company

Requirements
Must have
• Link folders. i.e.:
Home :: Users :: John Doe :: Test1
Nice to have
• Image Buttons
Should not have
• Noise

```html
<!DOCTYPE html>
<html lang="en">
<head>
<meta charset="utf-8">
<title>Keen Compass – Online Assessment</title>
<link rel="stylesheet" href="https://fonts.googleapis.com/css2?family=Open+Sans:wght@400;600;700&family=Josefin+Sans:wght@700&display=swap">
<style>
:root{
  --cream:#fefee0;
  --blue:#2371b9;
  --blue-light:#2e88cf;
  --blue-dark:#1b5fa3;
  --heading-blue:#175a98;
  --strip:#c3ecf1;
  --body-grey:#767676;
  --footer:#33332e;
  --footer-line:#d9d9a8;
  --white:#ffffff;
  --link-blue:#2f86d0;
  --ink:#1a1a1a;
}
*{margin:0;padding:0;box-sizing:border-box}
html,body{width:1200px;height:1094px;overflow:hidden;background:var(--cream)}
body{position:relative;font-family:"Open Sans",Arial,sans-serif}
.abs{position:absolute}
.top-bar{left:0;top:0;width:1200px;height:12px;background:var(--blue)}
.brand{left:38px;top:52px;height:60px;display:flex;align-items:center;gap:14px}
.brand-mark{width:48px;height:48px;border-radius:50%;background:var(--blue)}
.brand-name{font-size:34px;font-weight:400;color:var(--ink);letter-spacing:-.5px}
.main-nav{left:549px;top:66px;display:flex}
.main-nav a{width:154px;height:59px;display:flex;align-items:center;justify-content:center;
  color:var(--white);font-weight:600;font-size:22px;text-decoration:none;background:var(--blue-dark);
  border-left:1px solid #6aa6da}
.main-nav a:first-child{border-left:0;background:var(--blue-light)}
.hero{left:0;top:126px;width:1200px;height:328px;background:linear-gradient(90deg,#2372ba 0%,#2b84ca 55%,#2170b8 100%)}
.hero-strip{left:0;top:454px;width:1200px;height:14px;background:var(--strip)}
.hero-photo{left:89px;top:151px;width:425px;height:283px;background:linear-gradient(135deg,#e9eef2,#c9d3dc 60%,#aab4bd);
  box-shadow:2px 3px 4px rgba(0,0,0,.45);border:1px solid #fff}
.hero-title{left:594px;top:168px;font-family:"Josefin Sans","Open Sans",sans-serif;font-variant:small-caps;font-size:46px;
  color:var(--white);letter-spacing:.5px;text-shadow:1px 2px 2px rgba(0,0,0,.35)}
.hero-text{left:595px;top:240px;width:520px;font-size:19.5px;line-height:27px;color:var(--white)}
.btn{display:flex;align-items:center;justify-content:center;width:141px;height:35px;border-radius:3px;
  background:linear-gradient(#3b8ad2,#1a5597);color:var(--white);font-weight:700;font-size:17px;text-decoration:none;
  border:2px solid #e6e6e6;box-shadow:0 1px 3px rgba(0,0,0,.45);text-shadow:1px 1px 1px rgba(0,0,0,.6)}
.hero .btn,.hero-btn{left:595px;top:380px}
.feature{top:553px;width:365px}
.feature-icon{position:absolute;left:0;top:0;width:74px;height:74px}
.feature h2{position:absolute;left:90px;top:12px;font-size:19.5px;line-height:27px;font-weight:600;color:var(--heading-blue)}
.feature p{position:absolute;left:0;top:91px;width:365px;font-size:17px;line-height:30.5px;color:var(--body-grey)}
.feature .btn{position:absolute;left:0;top:278px}
.footer{left:0;top:904px;width:1200px;height:190px;background:var(--footer)}
.search{left:38px;top:935px;width:353px;height:27px;border-radius:14px;background:var(--white);
  font-family:Arial,sans-serif;font-size:14px;color:#333;padding-left:26px;display:flex;align-items:center}
.search svg{position:absolute}
.footer-lead{left:425px;top:928px;font-family:Arial,sans-serif;color:var(--white)}
.footer-lead strong{display:block;font-weight:400;font-size:16.5px}
.footer-lead span{display:block;font-size:12.5px;margin-top:5px}
.follow{left:923px;top:921px;font-family:Arial,sans-serif;font-size:14px;color:var(--white)}
.social{left:921px;top:946px;display:flex;gap:6px}
.social span{width:26px;height:26px;border-radius:50%;display:block}
.footer-rule{left:0;top:1003px;width:1200px;height:1px;background:var(--footer-line)}
.footer-note{left:38px;top:1015px;width:760px;font-family:Arial,sans-serif;font-size:13.5px;line-height:20px;color:var(--white)}
.footer-links{left:38px;top:1060px;font-family:Arial,sans-serif;font-size:14px;font-weight:700;color:var(--link-blue)}
.footer-links i{font-style:normal;color:#888;margin:0 9px;font-weight:400}
.legal{left:920px;top:1017px;font-family:Arial,sans-serif;font-size:14px;line-height:20px;color:var(--white);list-style:none}
.legal li::before{content:"";display:inline-block;border-left:4px solid #fff;border-top:3px solid transparent;border-bottom:3px solid transparent;margin-right:7px;vertical-align:1px}
</style>
</head>
<body>
<div class="abs top-bar"></div>

<header>
  <div class="abs brand"><span class="brand-mark"></span><span class="brand-name">Keen Compass</span></div>
  <nav class="abs main-nav">
    <a href="#">Home</a><a href="#">Users</a><a href="#">John Doe</a><a href="#">Test1</a>
  </nav>
</header>

<section class="abs hero"></section>
<div class="abs hero-strip"></div>
<div class="abs hero-photo" role="img" aria-label="Photo of a smiling businesswoman at an office desk with a computer, colleagues in the background"></div>
<h1 class="abs hero-title">Welcome to Keen Compass</h1>
<p class="abs hero-text">Keen Compass is an online assessment system based on the most recent neuroscience academic research. The system gathers tests that are applied in the selection and evaluation of employees.</p>
<a class="abs btn hero-btn" href="#">Read more</a>

<main>
  <article class="abs feature" style="left:38px">
    <svg class="feature-icon" viewBox="0 0 74 74" aria-hidden="true">
      <circle cx="37" cy="37" r="34" fill="#6f9fd8"/><circle cx="37" cy="37" r="28" fill="#eef2f6" stroke="#d0d8e0" stroke-width="2"/>
      <g stroke="#333" stroke-width="2"><line x1="37" y1="12" x2="37" y2="16"/><line x1="37" y1="58" x2="37" y2="62"/><line x1="12" y1="37" x2="16" y2="37"/><line x1="58" y1="37" x2="62" y2="37"/></g>
      <line x1="37" y1="37" x2="37" y2="19" stroke="#222" stroke-width="2.5"/><line x1="37" y1="37" x2="50" y2="43" stroke="#222" stroke-width="2.5"/>
      <circle cx="37" cy="37" r="2.5" fill="#222"/>
    </svg>
    <h2>Economic incentives<br>from various states</h2>
    <p>Vocent labores atomorum per an, ei sed voluptua efficiantur. Sit nobis efficiendi in. Ex eruditi imperdiet adipiscing vis, ius natum munere dolorem ne, ius invidunt menandri similique in. Ea duo iudico recusabo</p>
    <a class="btn" href="#">Read more</a>
  </article>

  <article class="abs feature" style="left:418px">
    <svg class="feature-icon" viewBox="0 0 74 74" aria-hidden="true">
      <circle cx="37" cy="37" r="27" fill="none" stroke="#e0e0e0" stroke-width="16"/>
      <g fill="none" stroke="#e2581c" stroke-width="16">
        <path d="M28 11.5A27 27 0 0 1 46 11.5"/><path d="M62.5 28A27 27 0 0 1 62.5 46"/>
        <path d="M46 62.5A27 27 0 0 1 28 62.5"/><path d="M11.5 46A27 27 0 0 1 11.5 28"/>
      </g>
    </svg>
    <h2>Economic comparisons<br>between the states</h2>
    <p>Vocent labores atomorum per an, ei sed voluptua efficiantur. Sit nobis efficiendi in. Ex eruditi imperdiet adipiscing vis, ius natum munere dolorem ne, ius invidunt menandri similique in. Ea duo iudico recusabo</p>
    <a class="btn" href="#">Read more</a>
  </article>

  <article class="abs feature" style="left:796px">
    <svg class="feature-icon" viewBox="0 0 74 74" aria-hidden="true">
      <g fill="#a9b0b6" stroke="#858d94" stroke-width="1.5">
        <g id="teeth">
          <rect x="31" y="2" width="12" height="14" rx="2"/><rect x="31" y="58" width="12" height="14" rx="2"/>
          <rect x="2" y="31" width="14" height="12" rx="2"/><rect x="58" y="31" width="14" height="12" rx="2"/>
        </g>
        <use href="#teeth" transform="rotate(45 37 37)"/>
        <circle cx="37" cy="37" r="25"/>
      </g>
      <circle cx="37" cy="37" r="10" fill="var(--cream)" stroke="#858d94" stroke-width="1.5"/>
    </svg>
    <h2>Companies moving out<br>of state: where and why</h2>
    <p>Vocent labores atomorum per an, ei sed voluptua efficiantur. Sit nobis efficiendi in. Ex eruditi imperdiet adipiscing vis, ius natum munere dolorem ne, ius invidunt menandri similique in. Ea duo iudico recusabo</p>
    <a class="btn" href="#">Read more</a>
  </article>
</main>

<footer>
  <div class="abs footer"></div>
  <div class="abs search">Tibique corpora senserit pro ad
    <svg style="left:290px;top:9px" width="14" height="9" viewBox="0 0 14 9" aria-hidden="true"><path d="M0 0h14L7 9z" fill="#555"/></svg>
    <svg style="left:318px;top:5px" width="18" height="18" viewBox="0 0 18 18" aria-hidden="true"><circle cx="7" cy="7" r="5.5" fill="none" stroke="#999" stroke-width="2"/><line x1="11" y1="11" x2="16.5" y2="16.5" stroke="#999" stroke-width="2.5"/></svg>
  </div>
  <div class="abs footer-lead"><strong>Vim ignota commodo te, eam saepe rationibus ut.</strong><span>Ex agam fastidii vim. An mea congue platonem facilisis. Mei te errem facilisis,</span></div>
  <div class="abs follow">Follow us:</div>
  <div class="abs social" aria-label="Social links">
    <span style="background:#e2722a"></span><span style="background:#5bb6e3"></span><span style="background:#2f4a8a"></span><span style="background:#b9bcc0"></span>
  </div>
  <div class="abs footer-rule"></div>
  <p class="abs footer-note">Usu vide iudicabit ex. Libris voluptua vix in, falli nobis necessitatibus per ut. An sit vidit invidunt definiebas, eum quas tacimates assueverit ex. Ut magna velit iracundia mea, ei reque homero principes duo.</p>
  <div class="abs footer-links">Libris<i>|</i>Legimus<i>|</i>Efficiantur<i>|</i>Feugiat<i>|</i>Tractatos<i>|</i>Corpora<i>|</i>Forensibus<i>|</i>Propriae</div>
  <ul class="abs legal"><li>Terms and Conditions</li><li>Privacy Policy</li></ul>
</footer>
</body>
</html>
```